Biz Card for Harrowfield Property Partners - HWPP

Harrowfield Property Partners is a commercial real estate acquisitions firm. We buy commercial property and need to raise capital from investors for each deal we buy. The vibe needs to be: give us your money, we will multiply it.
Our website: www.hrwpp-example.com
Competitors are: https://velmarholdings-example.com/, https://tribanquepartners-example.com/, http://www.ostrellecapital-example.com/
Target Market(s)
High Net Worth Individuals, Bankers, Insurance Companies, Commercial Real Estate Brokers.
Industry/Entity Type
Investment Banking
Contact Information for Business Card
Name, Title, Addess, Cell#, Office#, email, website
Requirements
Must have
- use one of our logos. See website for look and feel: www.hrwpp-example.com
Nice to have
- see website: www.hrwpp-example.com

```html
<!DOCTYPE html>
<html lang="en">
<head>
<meta charset="UTF-8">
<title>Harrowfield Property Partners – Business Card</title>
<link href="https://fonts.googleapis.com/css2?family=Montserrat:wght@400;500;700&display=swap" rel="stylesheet">
<style>
  :root {
    --stage: #1c1d21;
    --navy: #0a2340;
    --navy-tint: #16385a;
    --white: #ffffff;
    --muted: #c9d3df;
  }
  * { box-sizing: border-box; margin: 0; padding: 0; }
  html, body {
    width: 1200px; height: 800px; overflow: hidden;
    background: var(--stage);
    font-family: "Montserrat", sans-serif;
    color: var(--white);
  }
  .stage {
    width: 1200px; height: 800px;
    display: flex; flex-direction: column;
    align-items: center; justify-content: center; gap: 40px;
  }
  .card {
    position: relative;
    width: 560px; height: 320px;
    background: var(--navy);
    border-radius: 22px;
    overflow: hidden;
  }
  .card__halo {
    position: absolute;
    left: -90px; bottom: -210px;
    width: 420px; height: 420px;
    border-radius: 50%;
    background: var(--navy-tint);
  }
  .brand {
    display: flex; align-items: center; gap: 16px;
  }
  .brand__dot {
    width: 62px; height: 62px; border-radius: 50%;
    background: var(--white); flex: none;
  }
  .brand__name {
    font-weight: 400; color: var(--white); text-transform: uppercase;
    line-height: 1.15;
  }
  .brand__name .line-main { display: block; font-size: 25px; letter-spacing: 5px; }
  .brand__name .line-sub { display: block; font-size: 10.5px; letter-spacing: 4.2px; margin-top: 6px; }

  .card--front .brand {
    position: absolute; right: 40px; top: 92px;
  }

  .card--back .brand {
    position: absolute; left: 32px; top: 160px;
  }
  .card--back .brand__name .line-main { font-size: 19px; letter-spacing: 3.5px; }
  .card--back .brand__name .line-sub { font-size: 8.5px; letter-spacing: 3px; }
  .card--back .brand__dot { width: 52px; height: 52px; }

  .divider {
    position: absolute; left: 318px; top: 70px;
    width: 1px; height: 190px; background: var(--muted); opacity: .7;
  }
  .contact {
    position: absolute; left: 342px; top: 62px; right: 20px;
  }
  .contact__name { font-weight: 700; font-size: 16px; letter-spacing: .5px; text-transform: uppercase; }
  .contact__title { font-size: 11px; font-weight: 500; margin-top: 2px; }
  .contact__address { font-size: 10.5px; line-height: 1.45; margin-top: 16px; }
  .contact__list { list-style: none; margin-top: 14px; font-size: 10.5px; }
  .contact__list li { display: flex; align-items: center; gap: 7px; line-height: 1.7; }
  .contact__icon {
    width: 13px; height: 13px; border-radius: 50%;
    background: var(--white); flex: none;
    display: flex; align-items: center; justify-content: center;
  }
  .contact__icon svg { width: 8px; height: 8px; }
</style>
</head>
<body>
<main class="stage">

  <section class="card card--front" aria-label="Card front">
    <div class="card__halo"></div>
    <div class="brand">
      <span class="brand__dot"></span>
      <p class="brand__name"><span class="line-main">Harrowfield</span><span class="line-sub">Property Partners</span></p>
    </div>
  </section>

  <section class="card card--back" aria-label="Card back">
    <div class="brand">
      <span class="brand__dot"></span>
      <p class="brand__name"><span class="line-main">Harrowfield</span><span class="line-sub">Property Partners</span></p>
    </div>
    <div class="divider"></div>
    <div class="contact">
      <p class="contact__name">Rowan T. Ellery</p>
      <p class="contact__title">Executive Director</p>
      <p class="contact__address">PO BOX 418 Harbor Lane<br>2nd Street Dalton, USA</p>
      <ul class="contact__list">
        <li><span class="contact__icon"><svg viewBox="0 0 10 10"><path d="M2 1 L4 1 L4.6 3 L3.6 3.8 Q4.6 5.6 6.2 6.4 L7 5.4 L9 6 L9 8 Q8 9 6 8.4 Q2.4 6.8 1.2 3 Q1 1.8 2 1Z" fill="var(--navy)"/></svg></span>555-014-2270</li>
        <li><span class="contact__icon"><svg viewBox="0 0 10 10"><rect x="2.8" y="1" width="4.4" height="8" rx="1" fill="var(--navy)"/><rect x="3.6" y="2" width="2.8" height="5" fill="var(--white)"/></svg></span>555-014-8836</li>
        <li><span class="contact__icon"><svg viewBox="0 0 10 10"><rect x="1" y="2.5" width="8" height="5.5" rx=".6" fill="var(--navy)"/><path d="M1.4 3 L5 5.6 L8.6 3" stroke="var(--white)" stroke-width=".8" fill="none"/></svg></span>info@hrwpp-example.com</li>
        <li><span class="contact__icon"><svg viewBox="0 0 10 10"><circle cx="5" cy="5" r="3.8" fill="none" stroke="var(--navy)" stroke-width="1"/><path d="M1.2 5 H8.8 M5 1.2 Q2.6 5 5 8.8 M5 1.2 Q7.4 5 5 8.8" stroke="var(--navy)" stroke-width=".8" fill="none"/></svg></span>www.hrwpp-example.com</li>
      </ul>
    </div>
  </section>

</main>
</body>
</html>
```